Independent Midwife for a positive birth experience needs a vibrant, and elegant business card/logo

I need a business card design with a logo. The logo I would like to be able to use on my website (www.midwifemarisol.com) next to my name.
Therefore the design of the card and logo should suit the colours and design of the website. The title of the website and company is "Marisol Quenby Fairhurst, Midwife" but I'd like to have the business card title to be "Marisol Quenby Fairhurst - Independent Midwife" in bold letters, same script font as in my website.

I provide gold standard midwifery services, one-to-one tailored care, continuity of care throughout the entire pregnancy (antenatal care), the birth and after the birth (postnatal care), home birth, water birth, breast-feeding support, and birth preparation workshops. I also am certified and offer complementary therapies: pregnancy reflexology, rebozo techniques for optimal baby positioning.

The design should incorporate similar colours and style as the website and the "Marisol Quenby Fairhurst - Independent Midwife" on the card should include the same font as in the title of the website, however, in bold. The front of the card should have a logo, title and contact information (phone number 072639518, email marisol.fairhurst@lovantamail.com, website address www.midwifemarisol.com).
The back of the card to include the services I offer.

The logo: use of colour purple (varying shades), should communicate communicate warmth, kindness, compassion. It should convey that I'm a midwife who believes in fostering a trusting relationship with my clients and to provide them with a positive pregnancy and birth experience.

Target Market(s)

Pregnant women or women who are looking to book a private midwife for better birth experience and outcome

Industry/Entity Type

Baby

Contact Information for Business Card

Name and Title on front side together with contact details
The reverse side should have services/packages offered

Font styles to use
Script
Other font styles liked:
• similar script as in my website for name and title, and easy to read font for the rest of the words

Colors
b768aa
a54599
d2a4cc
ffffff

Requirements
Must have
• same font as title of website, but slightly bolder.
• similar design, colours, patterns as in website.
• Also include a gold accent colour somewhere in the design please.
Nice to have
• perhaps a logo of pregnant belly in profile or newborn baby icon

```html
<!DOCTYPE html>
<html lang="en">
<head>
<meta charset="utf-8">
<title>Marisol Quenby Fairhurst – Independent Midwife</title>
<link rel="stylesheet" href="https://fonts.googleapis.com/css2?family=Italianno&family=Cabin:wght@400;500&display=swap">
<style>
  :root {
    --purple-deep: #a54599;
    --purple-mid: #b768aa;
    --purple-soft: #d2a4cc;
    --white: #ffffff;
    --gold: #d8c23a;
    --gold-light: #f2ea7a;
    --gold-dark: #9a6a1e;
  }
  html, body {
    margin: 0;
    padding: 0;
    width: 1200px;
    height: 694px;
    overflow: hidden;
    background: var(--white);
  }
  .card {
    position: relative;
    width: 1200px;
    height: 694px;
    background: var(--white);
    overflow: hidden;
  }
  .corner-sweep {
    position: absolute;
    right: 0;
    bottom: 0;
    width: 330px;
    height: 340px;
  }
  .brand-mark {
    position: absolute;
    left: 60px;
    top: 250px;
    width: 270px;
    display: flex;
    flex-direction: column;
    align-items: center;
    gap: 14px;
    font-family: "Cabin", sans-serif;
    font-weight: 500;
    font-size: 26px;
    line-height: 1.2;
    color: var(--purple-mid);
    text-align: center;
  }
  .brand-mark__dot {
    width: 22px;
    height: 22px;
    border-radius: 50%;
    background: var(--purple-soft);
  }
  .title {
    position: absolute;
    left: 370px;
    top: 168px;
    width: 790px;
    margin: 0;
    text-align: center;
    font-family: "Italianno", cursive;
    font-weight: 400;
    color: var(--purple-deep);
    -webkit-text-stroke: 0.6px var(--purple-deep);
  }
  .title__name {
    display: block;
    font-size: 94px;
    line-height: 1;
    white-space: nowrap;
  }
  .title__role {
    display: block;
    margin-top: 10px;
    font-size: 78px;
    line-height: 1;
  }
  .contact {
    position: absolute;
    left: 340px;
    top: 452px;
    display: grid;
    grid-template-columns: 140px 1px auto;
    column-gap: 26px;
    font-family: "Cabin", sans-serif;
    font-size: 30px;
    line-height: 44px;
  }
  .contact__labels {
    text-align: right;
    color: var(--purple-deep);
  }
  .contact__divider {
    width: 3px;
    background: linear-gradient(to bottom, var(--gold) 0%, var(--gold) 30%, rgba(216, 194, 58, 0) 100%);
  }
  .contact__values {
    color: var(--purple-deep);
    font-weight: 500;
    letter-spacing: 0.2px;
  }
</style>
</head>
<body>
  <main class="card">
    <div class="brand-mark">
      <span class="brand-mark__dot"></span>
      <span class="brand-mark__name">Marisol Quenby<br>Fairhurst</span>
    </div>

    <h1 class="title">
      <span class="title__name">Marisol Quenby Fairhurst</span>
      <span class="title__role">Independent Midwife</span>
    </h1>

    <section class="contact">
      <div class="contact__labels">
        <div>phone</div>
        <div>email</div>
        <div>website</div>
      </div>
      <div class="contact__divider"></div>
      <div class="contact__values">
        <div>072639518</div>
        <div>marisol.fairhurst@lovantamail.com</div>
        <div>www.midwifemarisol.com</div>
      </div>
    </section>

    <svg class="corner-sweep" viewBox="0 0 330 340" aria-hidden="true">
      <defs>
        <linearGradient id="goldEdge" x1="0" y1="1" x2="1" y2="0">
          <stop offset="0" stop-color="#9a6a1e"/>
          <stop offset="0.35" stop-color="#c9a23a"/>
          <stop offset="0.6" stop-color="#f2ea7a"/>
          <stop offset="0.8" stop-color="#c9a23a"/>
          <stop offset="1" stop-color="#8a5a18"/>
        </linearGradient>
      </defs>
      <path d="M 0 340 Q 290 300 330 0 L 330 340 Z" fill="url(#goldEdge)"/>
      <path d="M 40 340 Q 300 300 330 40 L 330 340 Z" fill="#a54599"/>
    </svg>
  </main>
</body>
</html>
```